Brightwell Power Solutions

We'd like a web design that's beautiful and professional. We replace existing inefficient systems (mostly lighting at the moment but expanding) with highly efficient systems.

```html
<!DOCTYPE html>
<html lang="en">
<head>
<meta charset="utf-8">
<title>Brightwell Power Solutions – LED Lighting Solutions</title>
<link href="https://fonts.googleapis.com/css2?family=Cabin:wght@400;500&family=Oswald:wght@400&display=swap" rel="stylesheet">
<style>
:root{
  --green:#17ad4e;
  --green-dark:#0f8f3e;
  --ink:#333;
  --muted:#8a8a8a;
  --line:#d4d4d4;
  --panel:#e6e6e6;
  --white:#fff;
}
*{box-sizing:border-box;margin:0;padding:0}
html,body{width:1137px;height:1200px;overflow:hidden;background:var(--white)}
body{font-family:"Cabin",sans-serif;color:var(--ink);position:relative}
.page{position:relative;width:1137px;height:1200px}
.abs{position:absolute}

.hero-bg{left:0;top:0;width:1137px;height:531px;background:radial-gradient(ellipse at 50% 40%,#fff 0%,#f7f7f7 45%,#e9e9e9 100%)}

.topbar{left:94px;top:0;width:949px;height:50px;background:var(--green);border-radius:0 0 4px 4px}
.brand{left:108px;top:11px;width:81px;height:66px;background:var(--white);border:1px solid #999;display:flex;flex-direction:column;align-items:center;justify-content:center;gap:4px;padding:4px}
.brand-mark{width:18px;height:18px;background:var(--green)}
.brand-name{font-size:9px;line-height:1.15;text-align:center;color:var(--green-dark)}
.nav{right:116px;top:17px;display:flex;font-size:12px;color:var(--white);text-transform:uppercase;letter-spacing:.2px}
.nav span{padding:0 20px}
.nav span:last-child{padding-right:0}
.nav .sep{padding:0}
.phone-tab{left:767px;top:50px;width:253px;height:35px}
.phone-tab svg{position:absolute;left:0;top:0}
.phone-text{position:absolute;left:50px;top:7px;font-family:"Oswald",sans-serif;font-size:15px;color:var(--white);letter-spacing:-.3px}

.hero-title{left:117px;top:206px;font-size:52px;line-height:57px;color:var(--green);font-weight:400}
.hero-sub{left:117px;top:317px;width:330px;font-size:16px;line-height:20px;color:#444}
.hero-link{left:117px;top:385px;font-size:16px;color:var(--green)}
.sign{left:516px;top:166px;width:493px;height:279px;background:linear-gradient(160deg,#0c3a46 0%,#0a5463 45%,#0d2f38 100%);transform:skewY(-2deg);border-radius:2px}
.dots{top:240px}

.feature-band{left:94px;top:501px;width:949px;height:47px;background:var(--green);border-radius:4px 4px 0 0;color:var(--white);font-size:24px;text-align:center;line-height:47px}
.feature-panel{left:94px;top:548px;width:949px;height:291px;border:1px solid var(--line);border-top:none}
.feature-divider{left:417px;top:548px;width:1px;height:291px;background:var(--line)}
.lamps-title{left:109px;top:556px;font-size:17px;color:var(--green)}
.lamps-photo{left:108px;top:586px;width:286px;height:155px;background:linear-gradient(180deg,#142236 0%,#3b5fa3 45%,#b4566e 60%,#1b2a3a 100%)}
.lamps-text{left:110px;top:747px;width:287px;font-size:13.5px;line-height:17px;letter-spacing:.25px;color:var(--muted);text-align:justify}

.product{top:590px;width:160px;text-align:center}
.product-img{width:110px;height:114px;margin:0 auto;border-radius:6px;background:radial-gradient(circle at 50% 45%,#e0e0e0 0%,#bcbcbc 55%,#f5f5f5 100%)}
.product-name{margin-top:19px;font-size:15px;color:#555;white-space:nowrap}
.btn{display:inline-block;margin-top:7px;width:75px;height:22px;line-height:22px;background:var(--green);color:var(--white);font-family:"Oswald",sans-serif;font-size:12px;border-radius:2px;box-shadow:0 1px 1px rgba(0,0,0,.25)}

.slider{left:426px;top:791px}

.revolution{left:94px;top:867px;width:949px;height:134px;background:linear-gradient(90deg,#dcdcdc 0%,#f0f0f0 45%,#dadada 100%);border-radius:3px}
.rev-title{left:111px;top:871px;font-size:25px;color:var(--green)}
.rev-text{left:110px;top:900px;width:599px;font-size:14px;line-height:18.3px;color:#555;text-align:justify}
.help{left:740px;top:867px;width:270px;height:55px;background:var(--green);display:flex;align-items:center;padding-left:12px;gap:10px;color:var(--white);font-family:"Oswald",sans-serif;font-size:21px;letter-spacing:-.5px}

.footer-rule{left:94px;top:1041px;width:949px;height:1px;background:#999}
.footer-col{top:1066px;font-size:13px;line-height:17.2px;color:var(--muted)}
.footer-col span{display:block}
.social{left:928px;top:1066px;font-size:13px;color:var(--muted)}
.social-icons{display:flex;gap:10px;margin-top:14px;margin-left:8px}
.social-icons i{width:26px;height:26px;border-radius:50%;background:#4bb54a;display:block}
</style>
</head>
<body>
<div class="page">
  <div class="abs hero-bg"></div>

  <header>
    <div class="abs topbar"></div>
    <div class="abs brand"><span class="brand-mark"></span><span class="brand-name">Brightwell Power Solutions</span></div>
    <nav class="abs nav">
      <span>Home</span><span class="sep">|</span><span>Why LED?</span><span class="sep">|</span><span>Case Studies</span><span class="sep">|</span><span>FAQ</span><span class="sep">|</span><span>Energy Audit</span>
    </nav>
    <div class="abs phone-tab">
      <svg width="253" height="35" viewBox="0 0 253 35">
        <defs><linearGradient id="tabGrad" x1="0" y1="0" x2="0" y2="1"><stop offset="0" stop-color="#9a9a9a"/><stop offset="1" stop-color="#7d7d7d"/></linearGradient></defs>
        <path d="M0 0H253L243 35H12Z" fill="url(#tabGrad)"/>
        <path d="M35 10c-3 2-3 10 2 15l2-1-2-4-1 0c-1-2-1-4 0-6l1 0 1-4z" fill="#fff"/>
      </svg>
      <span class="phone-text">1-800-GLOW-LED (1-800-456-9533)</span>
    </div>
  </header>

  <section class="hero">
    <h1 class="abs hero-title" style="font-weight:400">LED LIGHTING<br>SOLUTIONS</h1>
    <p class="abs hero-sub">Excellence in Efficient &amp; Sustainable Design LED products available on Federal Supply List - FS-07F-0418M</p>
    <a class="abs hero-link">Learn More..</a>
    <div class="abs sign" role="img" aria-label="Illuminated blue LED sign panel reading LED SIGN"></div>
    <svg class="abs dots" style="left:66px" width="30" height="50" viewBox="0 0 30 50"><g fill="#111"><circle cx="26" cy="3" r="2.6"/><circle cx="20" cy="10" r="2.6"/><circle cx="13" cy="17" r="2.6"/><circle cx="6" cy="25" r="2.6"/><circle cx="13" cy="33" r="2.6"/><circle cx="20" cy="40" r="2.6"/><circle cx="26" cy="47" r="2.6"/><circle cx="22" cy="22" r="2.2"/><circle cx="16" cy="29" r="2.2"/></g></svg>
    <svg class="abs dots" style="left:1041px" width="30" height="50" viewBox="0 0 30 50"><g fill="#111"><circle cx="4" cy="3" r="2.6"/><circle cx="10" cy="10" r="2.6"/><circle cx="17" cy="17" r="2.6"/><circle cx="24" cy="25" r="2.6"/><circle cx="17" cy="33" r="2.6"/><circle cx="10" cy="40" r="2.6"/><circle cx="4" cy="47" r="2.6"/><circle cx="8" cy="22" r="2.2"/><circle cx="14" cy="29" r="2.2"/></g></svg>
  </section>

  <section class="featured">
    <h2 class="abs feature-band" style="font-weight:400">LED FEATURED SOLUTION</h2>
    <div class="abs feature-panel"></div>
    <div class="abs feature-divider"></div>
    <h3 class="abs lamps-title" style="font-weight:400">LED REPLACEMENT LAMPS</h3>
    <div class="abs lamps-photo" role="img" aria-label="Night aerial view of a stadium lit with colourful LED facade lighting"></div>
    <p class="abs lamps-text">Led Light bring energy savings to a variety of lighting applications. Our wide range of product offerings empower you to save through decreased energy.</p>

    <div class="abs product" style="left:405px"><div class="product-img" role="img" aria-label="LED bulb"></div><div class="product-name">Led System Tools</div><span class="btn">LEARN MORE</span></div>
    <div class="abs product" style="left:569px"><div class="product-img" role="img" aria-label="Portable LED work lights"></div><div class="product-name">Led Lightning Fixture</div><span class="btn">LEARN MORE</span></div>
    <div class="abs product" style="left:714px"><div class="product-img" role="img" aria-label="LED spot lamp"></div><div class="product-name">The Advantage</div><span class="btn">LEARN MORE</span></div>
    <div class="abs product" style="left:885px"><div class="product-img" role="img" aria-label="Round LED flood light"></div><div class="product-name">Free Lighting Audit</div><span class="btn">LEARN MORE</span></div>

    <svg class="abs slider" width="609" height="22" viewBox="0 0 609 22">
      <circle cx="11" cy="11" r="10" fill="none" stroke="var(--green)" stroke-width="2"/>
      <path d="M13 6l-5 5 5 5" fill="none" stroke="var(--green)" stroke-width="2.5"/>
      <line x1="43" y1="11" x2="580" y2="11" stroke="#ccc" stroke-width="1"/>
      <circle cx="57" cy="11" r="3.5" fill="var(--green)"/>
      <circle cx="598" cy="11" r="10" fill="none" stroke="var(--green)" stroke-width="2"/>
      <path d="M596 6l5 5-5 5" fill="none" stroke="var(--green)" stroke-width="2.5"/>
    </svg>
  </section>

  <section class="revolution-block">
    <div class="abs revolution"></div>
    <h2 class="abs rev-title" style="font-weight:400">A REVOLUTION IN LIGHTING</h2>
    <p class="abs rev-text">Our world-class engineers combine the best available components with innovative optical, electrical and thermal designs to create LED commercial lamps and lighting systems that are optimized for superior performance. We are superbly positioned to continue as an industry-leading innovator for years to come. Our world-class engineers combine the best available components with innovative optical.</p>
    <div class="abs help">QUESTIONS ? LET US HELP.
      <svg width="34" height="34" viewBox="0 0 34 34"><circle cx="17" cy="17" r="15" fill="none" stroke="#1d1d1d" stroke-width="3"/><path d="M12 13a5 5 0 1 1 7 4.5c-1.5.8-2 1.5-2 3" fill="none" stroke="#1d1d1d" stroke-width="3"/><circle cx="17" cy="25" r="2" fill="#1d1d1d"/></svg>
    </div>
  </section>

  <footer>
    <div class="abs footer-rule"></div>
    <div class="abs footer-col" style="left:107px"><span>LED</span><span>HID</span><span>Linear Fluorescent</span><span>CFL Non Integrated</span><span>Halogen</span><span>See all technologies</span></div>
    <div class="abs footer-col" style="left:296px"><span>Where to Buy</span><span>Pressroom</span><span>Corvane EliteNet</span><span>Halvex Technologies</span><span>About Corvane Lighting</span><span>Site Map</span></div>
    <div class="abs footer-col" style="left:514px"><span>Privacy Policy</span><span>Cookie Disclosure</span><span>Accessibility Statement</span><span>Terms of Use</span><span>Terms of Sale</span></div>
    <div class="abs footer-col" style="left:737px"><span>Where to Buy</span><span>Pressroom</span><span>Corvane EliteNet</span><span>Halvex Technologies</span><span>About Corvane Lighting</span><span>Site Map</span></div>
    <div class="abs social">Follow us at<div class="social-icons"><i></i><i></i></div></div>
  </footer>
</div>
</body>
</html>
```